Business Cards for a start up company

We are looking for a business card design for a start up company based in Ohio. The logo is attached. We are a healthcare company. We are open to all designs but want something professional but fun; creative, not boring

Industry/Entity Type

Healthcare

```html
<!DOCTYPE html>
<html lang="en">
<head>
<meta charset="utf-8">
<title>Bright Harbor Care – Business Cards</title>
<link href="https://fonts.googleapis.com/css2?family=Aldrich&family=Cormorant+Garamond:wght@500&family=Ubuntu:wght@400&display=swap" rel="stylesheet">
<style>
  :root {
    --bg: #ece9e4;
    --card-dark: #1b1b1c;
    --card-mid: #3a3839;
    --sky: #5bc3e2;
    --sky-light: #9fdcef;
    --wordmark: #a9dcef;
    --ink: #141414;
    --contact: #8ad2ea;
  }
  * { margin: 0; padding: 0; box-sizing: border-box; }
  html, body { width: 1200px; height: 1000px; overflow: hidden; }
  body { background: var(--bg); position: relative; }

  .card {
    position: absolute;
    overflow: hidden;
    box-shadow: 0 6px 18px rgba(0,0,0,0.35);
  }

  /* Front card */
  .card-front {
    left: 351px; top: 105px; width: 648px; height: 390px;
    background: radial-gradient(ellipse at 52% 45%, var(--card-mid) 0%, #242324 45%, var(--card-dark) 100%);
  }
  .brand {
    position: absolute; left: 0; right: 0; top: 160px;
    display: flex; align-items: center; justify-content: center; gap: 18px;
  }
  .brand-dot {
    width: 58px; height: 58px; border-radius: 50%;
    background: var(--sky);
  }
  .brand-name {
    font-family: "Cormorant Garamond", serif;
    font-weight: 500; font-size: 46px;
    color: var(--wordmark);
    letter-spacing: 0.5px;
  }

  /* Back card */
  .card-back {
    left: 96px; top: 520px; width: 690px; height: 430px;
    background: radial-gradient(ellipse at 55% 65%, var(--card-mid) 0%, #242324 50%, var(--card-dark) 100%);
  }
  .card-band { position: absolute; inset: 0; }
  .person { position: absolute; left: 44px; top: 80px; }
  .person-name {
    font-family: "Aldrich", sans-serif;
    font-size: 42px; letter-spacing: 3px; color: var(--ink);
  }
  .person-role {
    font-family: "Ubuntu", sans-serif;
    font-size: 15px; color: #1f3f4a; margin-top: 8px;
  }
  .contact {
    position: absolute; left: 64px; top: 282px;
    list-style: none;
    font-family: "Ubuntu", sans-serif; font-size: 15px; color: var(--contact);
  }
  .contact li { display: flex; align-items: flex-start; gap: 14px; margin-bottom: 14px; line-height: 1.4; }
  .contact svg { flex: none; margin-top: 1px; }
</style>
</head>
<body>

<section class="card card-front" aria-label="Card front">
  <div class="brand">
    <span class="brand-dot"></span>
    <span class="brand-name">Bright Harbor Care</span>
  </div>
</section>

<section class="card card-back" aria-label="Card back">
  <svg class="card-band" width="690" height="430" viewBox="0 0 690 430">
    <defs>
      <linearGradient id="bandFill" x1="0" y1="0" x2="1" y2="1">
        <stop offset="0" stop-color="#58c0e0"/>
        <stop offset="1" stop-color="#a6def0"/>
      </linearGradient>
    </defs>
    <path d="M0 0 H690 V18 C560 140 330 220 0 248 Z" fill="url(#bandFill)"/>
  </svg>

  <div class="person">
    <div class="person-name">Daniel Reyes</div>
    <div class="person-role">Chief Operating Officer</div>
  </div>

  <ul class="contact">
    <li>
      <svg width="22" height="22" viewBox="0 0 22 22"><circle cx="11" cy="11" r="11" fill="var(--contact)"/><rect x="5.5" y="7" width="11" height="8" fill="#1b1b1c"/><path d="M5.5 7 L11 11.5 L16.5 7" stroke="var(--contact)" stroke-width="1.2" fill="none"/></svg>
      <span>dreyes@brightharborcare.com</span>
    </li>
    <li>
      <svg width="22" height="22" viewBox="0 0 22 22"><circle cx="11" cy="11" r="11" fill="var(--contact)"/><path d="M5 9 Q11 4 17 9 L15 10 Q11 8 7 10 Z" fill="#1b1b1c"/><rect x="7" y="11" width="8" height="5" rx="1" fill="#1b1b1c"/></svg>
      <span>555-214-0673</span>
    </li>
    <li>
      <svg width="22" height="22" viewBox="0 0 22 22"><path d="M11 2 C7 2 5 5 5 8 C5 12 11 19 11 19 C11 19 17 12 17 8 C17 5 15 2 11 2 Z" fill="var(--contact)"/><circle cx="11" cy="8" r="2.2" fill="#1b1b1c"/></svg>
      <span>PO Box 412<br>Maple Falls, Ohio&nbsp;&nbsp;44105</span>
    </li>
  </ul>
</section>

</body>
</html>
```